VEXO Transaction Systems Corprate Web Site

Develop new corporate website and copywriting of web site. VEXO provides MPOS for banks and payment processors. Have included corporate background as well as marketing material from a bank payment processor that uses our products and services.

VEXO Transaction Systems Web design.... We are looking for a solid design to be followed by a complete proposal to complete entire site. The budget proposed is for design only to be followed by a complete budget.

tom questions Tom.Garrity@vexotsys.example

This is not really up to date as its our corporate website.... www.vexotransactionsystems.example

This is a customer that uses software that VEXO developed and that we have white labeled.
http://support.fenwara.example/en/fenwara-handheld/fenwara-handheld-max

We are open to new logo design (the current logo has many good design elements with the "Locked Tile"). We have provided what we use now in logo.zip. We use as example "Integrated Payment Solutions" as a tag line. We would also use Mobile as well as Transportation Solutions.
Updates

VEXO Transaction Systems Web design.... We are looking for a solid design to be followed by a complete proposal to complete entire site. The budget proposed is for design only to be followed by a complete budget.tom questions Tom.Garrity@vexotsys.example Added Sunday, September 13, 2015

Target Market(s)

Banks, payment processors and enterprise customers...

Coding

Coded - Design and coding required

Number of Pages Required

5+ page

Requirements
Must have
• VEXO Transaction Systems Web design.... We are looking for a solid design to be followed by a complete proposal to complete entire site. The budget proposed is for design only to be followed by a complete budget.
• tom questions Tom.Garrity@vexotsys.example
Nice to have

```html
<!DOCTYPE html>
<html lang="en">
<head>
<meta charset="utf-8">
<title>VEXO Transaction Systems</title>
<link rel="stylesheet" href="https://fonts.googleapis.com/css2?family=Oswald:wght@400;500;600&family=Open+Sans:wght@400;600;700&display=swap">
<style>
:root{
  --yellow:#f6c416;
  --yellow-dark:#e2b10c;
  --ink:#2a2a2a;
  --hero:#303234;
  --panel:#2e3033;
  --footer:#232426;
  --footer-bottom:#1a1b1c;
  --text:#555;
  --muted:#9a9a9a;
  --line:#e3e3e3;
  --white:#fff;
}
*{box-sizing:border-box;margin:0;padding:0}
html,body{width:1200px;height:2388px;overflow:hidden}
body{font-family:"Open Sans",Arial,sans-serif;color:var(--text);background:var(--white);position:relative}
ul{list-style:none}

/* header */
.site-header{height:112px;display:flex;align-items:center;padding:0 60px;background:var(--white)}
.brand{display:flex;align-items:center;gap:12px}
.brand-mark{width:38px;height:38px;border-radius:50%;background:var(--yellow)}
.brand-name{font-family:"Oswald",sans-serif;font-weight:600;font-size:44px;color:var(--ink);letter-spacing:1px}
.header-tools{margin-left:auto;display:flex;align-items:center;gap:28px}
.social{display:flex;gap:6px}
.social span{width:20px;height:20px;background:#3a5a98;border-radius:3px}
.social span:nth-child(2){background:#2ea3dd}
.social span:nth-child(3){background:#c9302c}
.social span:nth-child(4){background:#2a6ea8}
.contact-line{font-size:13px;color:var(--ink);line-height:20px;display:flex;align-items:center;gap:10px}
.contact-line .phone{font-weight:700;font-size:15px}
.contact-line svg{flex:none}
.login-btn{background:var(--ink);color:var(--white);font-size:12px;font-weight:700;padding:11px 22px;letter-spacing:.5px}

/* nav */
.main-nav{height:40px;background:var(--yellow);padding:0 60px;display:flex}
.main-nav a{display:flex;align-items:center;justify-content:center;font-size:12px;font-weight:600;color:var(--ink);text-decoration:none;text-transform:uppercase;width:150px}
.main-nav a.active{background:var(--ink);color:var(--white);width:90px}
.main-nav a:last-child{margin-left:auto}

/* hero */
.hero{height:468px;background:linear-gradient(180deg,#3a3c3e,#26282a);position:relative;padding:70px 0 0 120px}
.hero-copy{width:520px}
.hero h1{font-family:"Oswald",sans-serif;font-weight:500;font-size:40px;color:var(--white);line-height:1.1;white-space:nowrap}
.hero .sub{font-size:19px;color:var(--white);margin-top:8px}
.hero ul{margin-top:24px}
.hero li{color:#ddd;font-size:15px;margin-bottom:12px;display:flex;align-items:center;gap:12px}
.hero li::before{content:"";width:10px;height:10px;border:2px solid var(--yellow);border-radius:50%}
.btn-yellow{display:inline-block;background:var(--yellow);color:var(--ink);font-size:13px;font-weight:700;padding:14px 24px;margin-top:22px;text-transform:uppercase}
.hero-visual{position:absolute;left:680px;top:30px;width:430px;height:400px;background:linear-gradient(150deg,#e9ecef,#b8c0c6 55%,#4b5056);border-radius:6px}
.arrow{position:absolute;width:34px;height:54px;background:rgba(0,0,0,.35);display:flex;align-items:center;justify-content:center}
.hero .arrow.left{left:0;top:200px}
.hero .arrow.right{right:0;top:200px}

/* features */
.features{height:400px;position:relative;display:flex;justify-content:center;gap:28px;padding-top:90px;border-bottom:1px solid var(--line)}
.feature{width:230px;text-align:center}
.feature svg{display:block;margin:0 auto 18px}
.feature h3{font-size:17px;font-weight:600;color:var(--ink);line-height:1.3}
.feature p{font-size:12px;line-height:1.6;margin-top:10px;color:var(--muted)}
.features .arrow{background:#f1f1f1;top:170px}
.features .arrow.left{left:30px}
.features .arrow.right{right:30px}

/* white paper */
.white-paper{height:560px;background:var(--yellow);position:relative;overflow:hidden}
.white-paper .visual{position:absolute;left:80px;top:80px;width:500px;height:400px;background:linear-gradient(160deg,#f4f5f6,#c9ced3 60%,#6f7479);border-radius:6px}
.white-paper .panel{position:absolute;right:0;top:0;width:600px;height:560px;background:var(--panel);clip-path:polygon(70px 0,100% 0,100% 100%,0 100%);padding:110px 90px 0 120px}
.white-paper h2{font-family:"Oswald",sans-serif;font-weight:500;font-size:32px;color:var(--white);line-height:1.1;text-transform:uppercase}
.white-paper .tag{font-family:"Oswald",sans-serif;font-size:22px;color:var(--white)}
.wp-item{display:flex;gap:18px;margin-top:36px}
.wp-item .ic{width:56px;height:56px;border:2px solid #666;border-radius:50%;flex:none;display:flex;align-items:center;justify-content:center}
.wp-item h4{color:var(--white);font-size:15px;font-weight:600}
.wp-item p{color:#a8a8a8;font-size:12px;line-height:1.6;margin-top:6px}

/* testimonial */
.testimonial{height:370px;text-align:center;padding-top:60px}
.testimonial .portrait{width:100px;height:100px;border-radius:50%;margin:0 auto;background:linear-gradient(180deg,#c9ccd0,#7e858c)}
.testimonial blockquote{width:900px;margin:36px auto 0;font-size:14px;font-style:italic;line-height:1.8;color:#777}
.testimonial cite{display:block;margin-top:22px;font-style:normal;font-size:15px}
.testimonial cite b{color:var(--yellow-dark);font-weight:600}

/* partners */
.partners{height:90px;background:#f0f0f0;display:flex;align-items:center;justify-content:space-between;padding:0 120px}
.partners span{font-family:"Oswald",sans-serif;font-size:26px;font-weight:500;color:#9b9b9b;text-transform:uppercase}

/* footer */
.site-footer{height:300px;background:var(--footer);display:grid;grid-template-columns:300px 210px 150px 270px;gap:30px;padding:60px 60px 0 120px}
.site-footer h5{color:var(--white);font-size:13px;font-weight:700;text-transform:uppercase;margin-bottom:18px}
.site-footer p,.site-footer li{color:var(--muted);font-size:12px;line-height:1.9}
.newsletter form{display:flex;margin-top:18px}
.newsletter .field{width:190px;height:38px;background:#333;border:1px solid #444;color:#888;font-size:12px;padding:10px 12px}
.newsletter .submit{height:38px;background:var(--yellow);color:var(--ink);font-size:12px;font-weight:700;padding:11px 18px}
.contact li{display:flex;gap:10px;align-items:flex-start;white-space:nowrap}
.contact li::before{content:"";width:8px;height:8px;margin-top:8px;border-radius:50%;background:var(--yellow);flex:none}
.footer-bottom{height:48px;background:var(--footer-bottom);display:flex;flex-direction:column;align-items:center;justify-content:center;gap:6px}
.footer-bottom p{font-size:10px;color:#777}
.footer-bottom .social span{width:14px;height:14px;border-radius:50%;background:#444}
</style>
</head>
<body>

<header class="site-header">
  <div class="brand"><span class="brand-mark"></span><span class="brand-name">VEXO</span></div>
  <div class="header-tools">
    <div class="social"><span></span><span></span><span></span><span></span></div>
    <div class="contact-line">
      <svg width="26" height="26" viewBox="0 0 26 26"><circle cx="13" cy="13" r="12" fill="none" stroke="#2a2a2a" stroke-width="2"/><path d="M9 7l3 3-2 2c1 2 2 3 4 4l2-2 3 3-2 2c-5-1-9-5-10-10z" fill="#2a2a2a"/></svg>
      <div><div class="phone">1-855-000-4300</div><div>info@vexotransactionsystems.example</div></div>
    </div>
    <div class="login-btn">SECURE LOGIN</div>
  </div>
</header>

<nav class="main-nav">
  <a class="active">Home</a><a>About Us</a><a>White Paper</a><a>Solutions</a><a>Services</a><a>Blog</a><a>Contact Us</a>
</nav>

<section class="hero">
  <div class="hero-copy">
    <h1>Integrated Payment Solutions</h1>
    <p class="sub">VEXO Mobile and Portal Business Application's</p>
    <ul>
      <li>Merchant Business Portal and MPOS</li>
      <li>VEXO Management Portals Features</li>
      <li>Server, Web Services</li>
    </ul>
    <span class="btn-yellow">View Plans &amp; Features</span>
  </div>
  <div class="hero-visual" role="img" aria-label="Desktop monitor, tablet and phone showing the merchant management portal"></div>
  <div class="arrow left"><svg width="12" height="20"><path d="M10 2L2 10l8 8" fill="none" stroke="#fff" stroke-width="2"/></svg></div>
  <div class="arrow right"><svg width="12" height="20"><path d="M2 2l8 8-8 8" fill="none" stroke="#fff" stroke-width="2"/></svg></div>
</section>

<section class="features">
  <div class="arrow left"><svg width="12" height="20"><path d="M10 2L2 10l8 8" fill="none" stroke="#999" stroke-width="2"/></svg></div>
  <article class="feature">
    <svg width="96" height="104" viewBox="0 0 96 104"><polygon points="48,2 94,28 94,76 48,102 2,76 2,28" fill="var(--yellow)"/><rect x="28" y="38" width="40" height="28" rx="3" fill="none" stroke="#fff" stroke-width="3"/><line x1="28" y1="46" x2="68" y2="46" stroke="#fff" stroke-width="4"/></svg>
    <h3>Merchant Business<br>Portal and MPOS</h3>
    <p>Lorem ipsum dolor sit amet consectetur adipiscing elit sed do eiusmod tempor incididunt ut labore dolore</p>
  </article>
  <article class="feature">
    <svg width="96" height="104" viewBox="0 0 96 104"><polygon points="48,2 94,28 94,76 48,102 2,76 2,28" fill="var(--yellow)"/><path d="M40 34l22 22-10 2 6 12-5 2-6-12-7 7z" fill="#fff"/></svg>
    <h3>VEXO Management<br>Portals Features</h3>
    <p>Lorem ipsum dolor sit amet consectetur adipiscing elit sed do eiusmod tempor incididunt ut labore dolore</p>
  </article>
  <article class="feature">
    <svg width="96" height="104" viewBox="0 0 96 104"><polygon points="48,2 94,28 94,76 48,102 2,76 2,28" fill="var(--yellow)"/><path d="M30 44h32l-7-7M66 60H34l7 7" fill="none" stroke="#fff" stroke-width="4"/></svg>
    <h3>Server, Web Services<br>Payment Application</h3>
    <p>Lorem ipsum dolor sit amet consectetur adipiscing elit sed do eiusmod tempor incididunt ut labore dolore</p>
  </article>
  <article class="feature">
    <svg width="96" height="104" viewBox="0 0 96 104"><polygon points="48,2 94,28 94,76 48,102 2,76 2,28" fill="var(--yellow)"/><circle cx="48" cy="40" r="7" fill="#fff"/><circle cx="33" cy="62" r="6" fill="#fff"/><circle cx="63" cy="62" r="6" fill="#fff"/><path d="M48 47v7M48 54L33 62M48 54l15 8" stroke="#fff" stroke-width="3"/></svg>
    <h3>Network<br>Operations</h3>
    <p>Lorem ipsum dolor sit amet consectetur adipiscing elit sed do eiusmod tempor incididunt ut labore dolore</p>
  </article>
  <div class="arrow right"><svg width="12" height="20"><path d="M2 2l8 8-8 8" fill="none" stroke="#999" stroke-width="2"/></svg></div>
</section>

<section class="white-paper">
  <div class="visual" role="img" aria-label="Laptop, tablet, phone and card terminal showing the business application"></div>
  <div class="panel">
    <h2>Mobile and Portal Business</h2>
    <p class="tag">Application's Product White Paper</p>
    <div class="wp-item">
      <div class="ic"><svg width="26" height="22"><path d="M2 18l7-8 6 5 9-12" fill="none" stroke="#fff" stroke-width="2.5"/></svg></div>
      <div><h4>Business Snapshot</h4><p>Lorem ipsum dolor sit amet consectetur adipiscing elit sed do eiusmod tempor incididunt ut labore et dolore magna aliqua</p></div>
    </div>
    <div class="wp-item">
      <div class="ic"><svg width="26" height="24"><path d="M4 15v-3a9 9 0 0118 0v3" fill="none" stroke="#fff" stroke-width="2.5"/><rect x="2" y="14" width="5" height="8" rx="1" fill="#fff"/><rect x="19" y="14" width="5" height="8" rx="1" fill="#fff"/></svg></div>
      <div><h4>Analyze Your Data</h4><p>Lorem ipsum dolor sit amet consectetur adipiscing elit sed do eiusmod tempor incididunt ut labore et dolore magna aliqua</p></div>
    </div>
  </div>
</section>

<section class="testimonial">
  <div class="portrait" role="img" aria-label="Portrait photo of the client manager"></div>
  <blockquote>“ Lorem ipsum dolor sit amet, consectetur adipiscing elit, sed do eiusmod tempor incididunt ut labore et dolore magna aliqua. Ut enim ad minim veniam, quis nostrud exercitation ullamco laboris nisi ut aliquip ex ea commodo consequat. Duis aute irure dolor in reprehenderit in voluptate velit esse cillum dolore. ”</blockquote>
  <cite><b>John Doe</b> - Manager</cite>
</section>

<section class="partners">
  <span>Kestra</span><span>Lumbarro</span><span>Halden</span><span>Orvanta</span><span>Trelix</span><span>Bracken</span>
</section>

<footer class="site-footer">
  <div class="newsletter">
    <h5>Sign up for newsletter</h5>
    <p>Subscribe to our newsletter for updates, news and product releases from our team</p>
    <form><span class="field">Email</span><span class="submit">SUBSCRIBE</span></form>
  </div>
  <div>
    <h5>Our Services</h5>
    <ul><li>Merchant Business Portal and MPOS</li><li>VEXO Management Portal Features</li><li>Server, Web Service Payment</li><li>Transaction</li><li>Network Operations</li><li>Licensing Options</li></ul>
  </div>
  <div>
    <h5>Support</h5>
    <ul><li>Customer Portal</li><li>Support Desk</li><li>Partners</li><li>Site Map</li></ul>
  </div>
  <div class="contact">
    <h5>Contact Us</h5>
    <ul><li>48 Alder Lane, Suite 900, Fairport</li><li>1-855-000-4300</li><li>info@vexotransactionsystems.example</li></ul>
  </div>
</footer>

<div class="footer-bottom">
  <p>© 2015 VEXO Transaction Systems. All Rights Reserved.</p>
  <div class="social"><span></span><span></span><span></span><span></span></div>
</div>

</body>
</html>
```